Personal Training

The name of my company is Heron Fitness. I am looking for a design that will feature the 8 components I am utilizing in my workouts (strength, flexibility, agility, core, power, balance, cardiovacular, speed) and represent the spider. It is not essesstial to have a spider for my logo but would be nice. If a spider is used please do not use a logo like Gullwoman, a tarantula, or anything scary involving a spider (I have female clients who would get scared) lol
If you need me to provide more information please let me know. Feel free to check my website for ideas but ignore the pictures on my site as those are not pictures of me or clients
Thank you in advance!

Industry/Entity Type

Fitness

Contact Information for Business Card

Mark Delaney
Company Name: Heron Fitness
Tag line: 8 Keys To A Stronger You
Website: hernfit4.example
Email: mark@hernfit4.example
Cell: 555-314-2086

CQBL Certified Personal Trainer
CPR AED National Pulse Federation
B.A. Exercise Physiology W.K.R., 2004

```html
<!DOCTYPE html>
<html lang="en">
<head>
<meta charset="utf-8">
<title>Heron Fitness – Business Card</title>
<link rel="stylesheet" href="https://fonts.googleapis.com/css2?family=Arimo:wght@400;700&family=Libre+Baskerville:ital,wght@1,400;1,700&display=swap">
<style>
  :root {
    --backdrop: #e2e2e2;
    --card-white: #ffffff;
    --card-grey: #b4b4b4;
    --card-black: #050505;
    --brand-red: #d9453f;
    --stripe-red: #e59a9a;
    --stripe-pale: #f6dada;
    --mark-grey: #8c8c8c;
    --ink-dark: #1d1d1d;
    --ink-light: #f2f2f2;
  }
  * { box-sizing: border-box; margin: 0; padding: 0; }
  html, body {
    width: 1200px; height: 960px; overflow: hidden;
    background: var(--backdrop);
    font-family: "Arimo", Arial, sans-serif;
  }
  .card {
    position: absolute;
    left: 220px;
    width: 760px; height: 434px;
    border-radius: 26px;
    overflow: hidden;
  }

  /* ---------- Front ---------- */
  .card-front { top: 36px; background: var(--card-white); }
  .front-band {
    position: absolute; left: 0; right: 0;
    height: 22px;
    background: repeating-linear-gradient(180deg, var(--stripe-red) 0 1px, var(--stripe-pale) 1px 3px);
  }
  .front-band.upper { top: 248px; }
  .front-grey {
    position: absolute; left: 0; right: 0; top: 270px; bottom: 0;
    background: var(--card-grey);
  }
  .front-band.lower { top: 326px; }
  .front-brand {
    position: absolute; top: 52px; left: 0; right: 0;
    display: flex; flex-direction: column; align-items: center;
  }
  .brand-disc {
    width: 132px; height: 132px; border-radius: 50%;
    background: var(--brand-red);
  }
  .brand-name {
    margin-top: 12px;
    font-size: 17px; letter-spacing: 0.5px;
    color: var(--ink-dark); text-transform: uppercase;
  }
  .tagline {
    margin-top: 6px;
    display: flex; align-items: center; gap: 10px;
    font-family: "Libre Baskerville", Georgia, serif;
    font-style: italic; font-weight: 700;
    font-size: 16px; color: var(--ink-dark);
  }
  .tagline .accent { color: var(--brand-red); font-weight: 400; font-size: 18px; }
  .marks { display: inline-flex; gap: 2px; }
  .marks i { display: block; width: 5px; height: 12px; }
  .marks i:nth-child(1) { background: var(--mark-grey); }
  .marks i:nth-child(2) { background: var(--brand-red); }

  /* ---------- Back ---------- */
  .card-back { top: 506px; background: var(--card-black); color: var(--ink-light); }
  .trainer {
    position: absolute; top: 28px; left: 24px;
  }
  .trainer-name {
    display: flex; align-items: center; gap: 6px;
    font-size: 19px;
  }
  .trainer-name .surname { color: var(--brand-red); }
  .credentials {
    margin-left: 66px; margin-top: 2px;
    font-size: 15px; line-height: 1.2;
  }
  .contacts {
    position: absolute; top: 184px; left: 112px;
    list-style: none;
    display: flex; flex-direction: column; gap: 10px;
  }
  .contacts li {
    display: flex; align-items: center; gap: 14px;
    font-size: 15px;
  }
  .contacts svg { width: 32px; height: 32px; flex: none; }
  .back-brand {
    position: absolute; top: 108px; right: 96px;
    display: flex; flex-direction: column; align-items: center;
  }
  .back-brand .brand-disc { width: 146px; height: 146px; }
  .back-brand .brand-name {
    margin-top: 10px; font-size: 9px; color: var(--ink-light);
  }
  .back-rule {
    position: absolute; left: 60px; right: 40px; top: 360px; height: 1px;
    background: linear-gradient(90deg, transparent, var(--brand-red) 40%, var(--brand-red) 70%, transparent);
  }
</style>
</head>
<body>

<section class="card card-front" aria-label="Business card front">
  <div class="front-band upper"></div>
  <div class="front-grey"></div>
  <div class="front-band lower"></div>
  <div class="front-brand">
    <div class="brand-disc"></div>
    <p class="brand-name">Heron Fitness</p>
    <p class="tagline">
      <span class="marks"><i></i><i></i></span>
      <span>8 Keys To A Stronger <span class="accent">You</span></span>
      <span class="marks"><i></i><i></i></span>
    </p>
  </div>
</section>

<section class="card card-back" aria-label="Business card back">
  <div class="trainer">
    <p class="trainer-name">
      <span class="marks"><i></i><i></i></span>
      <span>Mark <span class="surname">Delaney</span></span>
      <span class="marks"><i></i><i></i></span>
    </p>
    <p class="credentials">
      CQBL Certified Personal Trainer<br>
      CPR AED National Pulse Federation<br>
      B.A. Exercise Physiology W.K.R., 2004
    </p>
  </div>

  <ul class="contacts">
    <li>
      <svg viewBox="0 0 32 32" aria-hidden="true">
        <rect x="6" y="6" width="20" height="20" transform="rotate(45 16 16)" fill="#d9453f"/>
        <rect x="12.5" y="9" width="7" height="14" rx="1.2" fill="#fff"/>
        <rect x="13.5" y="10.5" width="5" height="9" fill="#d9453f"/>
      </svg>
      <span>555-314-2086</span>
    </li>
    <li>
      <svg viewBox="0 0 32 32" aria-hidden="true">
        <rect x="6" y="6" width="20" height="20" transform="rotate(45 16 16)" fill="#d9453f"/>
        <rect x="10" y="12" width="12" height="8" fill="#fff"/>
        <path d="M10 12 L16 17 L22 12" fill="none" stroke="#d9453f" stroke-width="1.2"/>
      </svg>
      <span>mark@hernfit4.example</span>
    </li>
    <li>
      <svg viewBox="0 0 32 32" aria-hidden="true">
        <rect x="6" y="6" width="20" height="20" transform="rotate(45 16 16)" fill="#d9453f"/>
        <g fill="none" stroke="#fff" stroke-width="1.1">
          <circle cx="16" cy="16" r="6"/>
          <ellipse cx="16" cy="16" rx="2.6" ry="6"/>
          <line x1="10" y1="16" x2="22" y2="16"/>
        </g>
      </svg>
      <span>hernfit4.example</span>
    </li>
    <li>
      <svg viewBox="0 0 32 32" aria-hidden="true">
        <rect x="6" y="6" width="20" height="20" transform="rotate(45 16 16)" fill="#d9453f"/>
        <path d="M16 23 C13 19 11.5 17 11.5 14.5 A4.5 4.5 0 0 1 20.5 14.5 C20.5 17 19 19 16 23 Z" fill="#fff"/>
        <circle cx="16" cy="14.5" r="1.6" fill="#d9453f"/>
      </svg>
      <span>Address... here....</span>
    </li>
  </ul>

  <div class="back-brand">
    <div class="brand-disc"></div>
    <p class="brand-name">Heron Fitness</p>
  </div>

  <div class="back-rule"></div>
</section>

</body>
</html>
```